Welcome Booklet for Plastic Surgery Patients

I need a welcome booklet for a plastic surgery office. We already have the content and a logo, we just need help putting together a design for the booklet. The book details the types of procedures offered by the doctor (Loriane Whitcombe M.D). Attached is a booklet from another doctor as a reference point (Varnholt Plastic Surgery).
We would like it to be mainly white, gray, black with a little bit of pink as a reflection of the doctors work with Breast Cancer.

Target Market(s)

It is meant to be informative for women seeking Breast Reconstruction who have been diagnosed with breast cancer.

Industry/Entity Type

Plastic

Font styles to use
Other font styles liked:
• century gothic

Colors
7f7f7f
ffffff
1b1b1b
eda3c7

Requirements
Must have
• - Address shown on the back page (we have two locations) -
• 218 S Wexmoor Suite 306 Beverly Hills CA 90211
• 17842 Pellham Street Suite 209 Torrance CA 90503
• - The personal picture of Dr. Whitcombe needs to be on the welcome page
• - Pages 3-7 should have breast reconstruction at the top
• - Page 8 should have face at the top
• - Page 9 Should have body at the top
• - Attached is the image we want for the cover
Nice to have
• -The names of the procedures to stand out
• - For the most part we want a very clean look
• - The logo has been uploaded if there is a good place to place it

```html
<!DOCTYPE html>
<html lang="en">
<head>
<meta charset="utf-8">
<title>Welcome Booklet – Pages 9 and 10</title>
<link href="https://fonts.googleapis.com/css2?family=Didact+Gothic&display=swap" rel="stylesheet">
<style>
  :root {
    --stage: #000000;
    --paper: #ffffff;
    --label: #ffffff;
    --accent-pink: #eda3c7;
    --body-grey: #8f8f8f;
    --photo-warm: #ead9c8;
    --photo-light: #f6efe8;
  }
  * { margin: 0; padding: 0; box-sizing: border-box; }
  html, body {
    width: 1200px;
    height: 739px;
    overflow: hidden;
    background: var(--stage);
    font-family: "Didact Gothic", "Century Gothic", sans-serif;
  }
  .canvas {
    position: relative;
    width: 1200px;
    height: 739px;
    background: var(--stage);
  }
  .page-label {
    position: absolute;
    top: 82px;
    width: 120px;
    margin-left: -60px;
    text-align: center;
    color: var(--label);
    font-size: 17px;
    line-height: 20px;
  }
  .page-label--left { left: 275px; }
  .page-label--right { left: 853px; }

  .spread {
    position: absolute;
    left: 59px;
    top: 139px;
    width: 1036px;
    height: 517px;
    background: var(--paper);
    overflow: hidden;
  }
  .procedure__title {
    position: absolute;
    left: 33px;
    color: var(--accent-pink);
    font-weight: 400;
    font-size: 20px;
    line-height: 22px;
    white-space: nowrap;
  }
  .procedure__text {
    position: absolute;
    left: 33px;
    width: 460px;
    color: var(--body-grey);
    font-size: 9.7px;
    line-height: 14.8px;
  }
  .procedure__line { display: block; white-space: nowrap; }
  .procedure--tummy .procedure__title { top: 95px; }
  .procedure--tummy .procedure__text { top: 146px; }
  .procedure--lipo .procedure__title { top: 300px; }
  .procedure--lipo .procedure__text { top: 352px; }

  .body-photo {
    position: absolute;
    left: 550px;
    top: 0;
    width: 386px;
    height: 517px;
    background: linear-gradient(180deg, var(--photo-warm) 0%, var(--photo-light) 100%);
  }
</style>
</head>
<body>
<div class="canvas">
  <div class="page-label page-label--left">Page 9</div>
  <div class="page-label page-label--right">Page 10</div>

  <section class="spread">
    <article class="procedure procedure--tummy">
      <h2 class="procedure__title">Tummy tuck</h2>
      <p class="procedure__text">
        <span class="procedure__line">Navigating insurance policies can be daunting and stressful, so our staff is devoted to ensuring</span>
        <span class="procedure__line">that our patients are secure and informed about their options and that their medical team is</span>
        <span class="procedure__line">advocating on their behalf. Because of legislation passed in 1998, insurance companies must</span>
        <span class="procedure__line">cover breast reconstruction following mastectomy. By law a woman is entitled to reconstructed</span>
        <span class="procedure__line">breasts, breast symmetry and any future surgery needed to revise the primary reconstruction.</span>
        <span class="procedure__line">We work to ensure our patients completely understand their right to coverage as well as the</span>
        <span class="procedure__line">financial implications of any decisions they choose to make. We want to make sure that breast</span>
        <span class="procedure__line">reconstruction is affordable and accessible to all women.</span>
      </p>
    </article>

    <article class="procedure procedure--lipo">
      <h2 class="procedure__title">Liposuction</h2>
      <p class="procedure__text">
        <span class="procedure__line">Whether because of inactivity, less than fantastic dietary habits, or just as an unfortunate and</span>
        <span class="procedure__line">often inescapable part of growing older, many people find themselves developing a bit of</span>
        <span class="procedure__line">extra, unwanted fat here and there. Liposuction is an excellent technique to sculpt the body</span>
        <span class="procedure__line">that you have always dreamed of and attack stubborn areas of fat. Dr. Whitcombe is well known</span>
        <span class="procedure__line">for her liposculpture technique and is one of the best in Beverly Hills.</span>
      </p>
    </article>

    <div class="body-photo" role="img" aria-label="Photograph of a slim woman's torso in white underwear, cropped from shoulders to thighs, on a white background"></div>
  </section>
</div>
</body>
</html>
```